Onlineshop VORMA braucht ein Design!
Zielgruppe
Wir entwickeln innovative Produkte. Für dieses Projekt haben wir 2 Zielgruppen: Kinder und Erwachsene.
Hallo,
wir haben ein neuartiges Tragesystem entwickelt, das dem Träger der Tasche das Tragen erleichtert. Im Moment arbeiten wir daran, dieses System für eine eigene Schultaschenlinie zu verwenden. Später wollen wir unsere Produktpalette erweitern und ebenso Zubehör hierzu(z.B. Regenschirm, Mütze etc.) mit anbieten. Als weiterer Schritt sind zudem auch andere Taschen (z.B. Rucksäcke) für Erwachsene geplant.
Unser Produkt ist einmalig und genau deshalb möchten wir eine Homepage mit Shopware 4 Community Edition eine prägnanten und übersichtlichen Shop, sowie ein Blog erstellen.
Das Logo für unser Schultaschenprojekt befindet sich im Anhang und kann farblich angepasst werden. Wir benötigen einen kindergerechten, gleichzeitig seriösen Internetauftritt und es kann auch gerne ein komplettes Template erstellt werden für Shopware 4 oder ein Design-Vorschlag (Photoshop) eingebracht werden.
Wir bitten euch die Photoshop-Design Vorlagen ohne verbundene Ebenen und Pfade anzulegen. Bei Templates, bitten wir um eine genauere detaillierte Information zum Aufbau, Struktur etc..

```html
<!DOCTYPE html>
<html lang="de">
<head>
<meta charset="utf-8">
<title>VORMA – Onlineshop</title>
<link href="https://fonts.googleapis.com/css2?family=Roboto:wght@300;400;500;700&display=swap" rel="stylesheet">
<style>
:root{
  --orange:#e8590c;
  --orange-light:#f0883e;
  --page:#e6e6e6;
  --panel:#ffffff;
  --text:#555555;
  --muted:#777777;
  --dark:#333333;
  --darker:#1f1f1f;
  --peach:#fbe9e0;
  --rule:#e2e2e2;
  --badge:#d9d9d9;
}
*{box-sizing:border-box;margin:0;padding:0}
html,body{width:965px;height:1200px;overflow:hidden}
body{background:var(--page);font-family:'Roboto',sans-serif;font-weight:300;color:var(--text);position:relative}
.abs{position:absolute}
a{color:inherit;text-decoration:none}

.brand{left:155px;top:6px;font-size:34px;font-weight:700;color:var(--orange);letter-spacing:2px}
.account{top:8px;font-size:8px;color:var(--muted);display:flex;align-items:center;gap:4px}
.account .icon{width:19px;height:19px;border-radius:50%;background:#444;display:flex;align-items:center;justify-content:center}

.mainnav{left:138px;top:54px;width:689px;height:29px;background:linear-gradient(#f29a55,var(--orange) 60%,#d9570f);box-shadow:0 2px 3px rgba(0,0,0,.25);border-radius:2px}
.mainnav ul{list-style:none;display:flex;position:absolute;left:16px;top:8px;font-size:9.5px;color:#fff;font-weight:400}
.mainnav li{padding:0 11px;border-right:1px solid rgba(255,255,255,.35)}
.mainnav li:first-child{padding-left:0}
.mainnav li:last-child{border:none}
.search{position:absolute;left:535px;top:5px;width:146px;height:18px;background:linear-gradient(#ccc,#e4e4e4);border-radius:2px;border:1px solid #b5b5b5}
.search svg{position:absolute;right:4px;top:3px}
.search:after{content:"";position:absolute;right:20px;top:3px;width:1px;height:11px;background:#999}

.hero{left:139px;top:103px;width:688px;height:227px;box-shadow:0 2px 4px rgba(0,0,0,.3);background:var(--peach)}
.hero-photo{position:absolute;left:0;top:0;width:510px;height:227px;background:linear-gradient(180deg,#9cb7d4 0%,#5d7f4a 35%,#7c9e45 70%,#4d6a2a 100%)}
.hero-photo:after{content:"";position:absolute;left:290px;top:0;width:220px;height:227px;background:linear-gradient(90deg,rgba(120,110,190,0) 0%,#8a82c9 30%,#2b2b35 70%,#3a3a3a 100%)}
.teasers{position:absolute;left:510px;top:0;width:178px}
.teaser{height:57px;border-bottom:1px solid #e7cdbf;position:relative}
.teaser.active{background:#4a4a4a}
.teaser.active:before{content:"";position:absolute;left:-1px;top:24px;border:4px solid transparent;border-left-color:var(--orange)}
.teaser .thumb{position:absolute;left:6px;top:8px;width:55px;height:41px}
.teaser.active .thumb{outline:2px solid var(--orange)}
.teaser p{position:absolute;left:68px;top:7px;font-size:8.8px;line-height:11.5px;color:var(--muted)}
.teaser.active p{color:#eee}
.teaser b{color:var(--orange);font-weight:500;display:block}

.panel{left:138px;width:689px;background:var(--panel);box-shadow:0 2px 4px rgba(0,0,0,.3)}
.panel:before{content:"";position:absolute;left:0;top:0;width:100%;height:9px;background:linear-gradient(var(--orange-light),var(--orange))}
.products{top:358px;height:239px}
.product{position:absolute;top:42px;width:155px;height:158px}
.product h3{font-size:11px;font-weight:500;color:var(--orange)}
.product .price{font-size:8.5px;color:var(--muted);margin-top:2px}
.product .shot{position:absolute;top:27px;left:12px;width:118px;height:124px;border-radius:8px}
.product .more{position:absolute;right:10px;top:136px;font-size:10.5px;font-weight:500;color:var(--orange)}
.sale{position:absolute;left:114px;top:20px;width:34px;height:34px;border-radius:50%;background:var(--orange);color:#fff;font-size:7px;font-weight:700;display:flex;align-items:center;justify-content:center}
.divider{position:absolute;width:1px;background:var(--rule)}
.arrow{position:absolute;top:115px;width:18px;height:18px;background:#c8c8c8;display:flex;align-items:center;justify-content:center}

.info{top:625px;height:324px}
.info h2{position:absolute;font-size:12px;font-weight:500;color:var(--orange)}
.info p.copy{position:absolute;width:292px;font-size:11px;line-height:13.2px;color:var(--muted)}
.newsletter-form{position:absolute;top:266px;left:22px;display:flex;gap:9px}
.newsletter-form .field{width:148px;height:18px;border:1px solid #aaa;background:#dcdcdc;font-size:8.5px;padding:3px 5px;color:var(--muted)}
.newsletter-form .send{width:41px;height:18px;background:linear-gradient(var(--orange-light),var(--orange));color:#fff;font-size:9px;font-weight:500;display:flex;align-items:center;justify-content:center}
.news{position:absolute;left:355px;width:325px;height:120px}
.news .date{position:absolute;left:0;top:0;width:29px;height:29px;border-radius:50%;background:var(--orange);color:#fff;font-size:8.5px;line-height:9.5px;text-align:center;padding-top:5px}
.news h4{position:absolute;left:50px;top:9px;width:270px;font-size:10.5px;line-height:13px;font-weight:500;color:var(--orange)}
.news p{position:absolute;left:0;top:48px;width:325px;font-size:11px;line-height:13.2px;color:var(--muted)}
.news .more{position:absolute;right:0;top:103px;font-size:10.5px;font-weight:500;color:var(--orange)}

.footer{left:0;top:984px;width:965px;height:150px;background:var(--dark);color:#eee}
.footer h5{position:absolute;top:20px;font-size:12px;font-weight:500;color:var(--orange)}
.footer .col{position:absolute;font-size:10.5px;line-height:13.2px}
.fdiv{position:absolute;top:15px;width:1px;height:114px;background:#ccc}
.pay{position:absolute;width:29px;height:18px;border-radius:2px;background:var(--badge);color:var(--dark);font-size:6px;font-weight:400;display:flex;align-items:center;justify-content:center}
.social{position:absolute;top:129px;width:16px;height:16px;border-radius:2px;background:#8a8a8a}
.cats{list-style:none;font-size:9.8px;line-height:13.8px}
.cats li:before{content:"›";color:var(--orange);font-weight:700;margin-right:2px}
.tweet-date{color:var(--orange);font-size:9.8px}
.bottom{left:0;top:1134px;width:965px;height:66px;background:var(--darker);color:#eee;font-size:10.5px}
.bottom .legal{position:absolute;left:160px;top:28px}
.bottom .links{position:absolute;right:157px;top:28px}
.bottom .links span{margin:0 6px;color:#999}
</style>
</head>
<body>

<header>
  <div class="abs brand">VORMA</div>
  <div class="abs account" style="left:661px"><span class="icon"><svg width="10" height="10" viewBox="0 0 10 10"><circle cx="3" cy="7" r="2" fill="none" stroke="#fff" stroke-width="1.3"/><path d="M4.5 5.5 9 1M7 3l1.5 1.5" stroke="#fff" stroke-width="1.3"/></svg></span>Logout</div>
  <div class="abs account" style="left:720px"><span class="icon"><svg width="11" height="10" viewBox="0 0 11 10"><path d="M0 1h2l1.5 5h5.5l1-3.5H3" fill="none" stroke="#fff" stroke-width="1.2"/><circle cx="4" cy="8.5" r="1" fill="#fff"/><circle cx="8" cy="8.5" r="1" fill="#fff"/></svg></span>Mein Warenkorb (0,00 €)</div>
  <nav class="abs mainnav">
    <ul><li>Home</li><li>Über uns</li><li>Shop</li><li>Blog</li><li>Kontakt</li></ul>
    <div class="search"><svg width="9" height="9" viewBox="0 0 9 9"><circle cx="3.5" cy="3.5" r="2.7" fill="none" stroke="#666" stroke-width="1.2"/><path d="M5.5 5.5 8.5 8.5" stroke="#666" stroke-width="1.4"/></svg></div>
  </nav>
</header>

<section class="abs hero">
  <div class="hero-photo" role="img" aria-label="Wanderrucksack vor Bergpanorama mit grünem Tal"></div>
  <div class="teasers">
    <div class="teaser active"><div class="thumb" role="img" aria-label="Steinturm am Strand" style="background:linear-gradient(#4a8fd8,#d9c08a)"></div><p><b>Im ratur sim re voluptam</b>adi conserr uptatet reictis quatem litasincia quatur.</p></div>
    <div class="teaser"><div class="thumb" role="img" aria-label="Ledertaschen im Regal" style="background:linear-gradient(135deg,#e8e8e8,#5a3a28 60%,#2a2a2a)"></div><p><b>Im ratur sim re voluptam</b>adi conserr uptatet reictis quatem litasincia quatur.</p></div>
    <div class="teaser"><div class="thumb" role="img" aria-label="Kind mit Schultasche vor blauem Himmel" style="background:linear-gradient(#6aa6e0,#dfe8f2)"></div><p><b>Im ratur sim re voluptam</b>adi conserr uptatet reictis quatem litasincia quatur.</p></div>
    <div class="teaser"><div class="thumb" role="img" aria-label="Frau mit Handtasche" style="background:linear-gradient(90deg,#8a7d6a,#d8cfc0,#8a7d6a)"></div><p><b>Im ratur sim re voluptam</b>adi conserr uptatet reictis quatem litasincia quatur.</p></div>
  </div>
</section>

<section class="abs panel products">
  <div class="arrow" style="left:1px"><svg width="7" height="9" viewBox="0 0 7 9"><path d="M5.5 1 2 4.5 5.5 8" fill="none" stroke="#fff" stroke-width="2"/></svg></div>
  <div class="arrow" style="left:670px"><svg width="7" height="9" viewBox="0 0 7 9"><path d="M1.5 1 5 4.5 1.5 8" fill="none" stroke="#fff" stroke-width="2"/></svg></div>
  <div class="product" style="left:22px"><h3>Im ratur sim re voluptam</h3><div class="price">xx,xx €</div><div class="shot" role="img" aria-label="Schwarz-grauer Rucksack" style="background:radial-gradient(#7a7a7a,#2b2b2b 60%,#fff 72%)"></div><div class="sale">SALE</div><a class="more">weiter ...</a></div>
  <div class="divider" style="left:177px;top:42px;height:162px"></div>
  <div class="product" style="left:189px"><h3>Im ratur sim re voluptam</h3><div class="price">xx,xx €</div><div class="shot" role="img" aria-label="Rote Handtasche" style="background:radial-gradient(#d2343a,#b01e26 55%,#fff 70%)"></div><a class="more">weiter ...</a></div>
  <div class="divider" style="left:344px;top:42px;height:162px"></div>
  <div class="product" style="left:356px"><h3>Im ratur sim re voluptam</h3><div class="price">xx,xx €</div><div class="shot" role="img" aria-label="Lila Schulranzen" style="background:radial-gradient(#9c9fe6,#7f82d8 55%,#fff 70%)"></div><a class="more">weiter ...</a></div>
  <div class="divider" style="left:511px;top:42px;height:162px"></div>
  <div class="product" style="left:522px"><h3>Im ratur sim re voluptam</h3><div class="price">xx,xx €</div><div class="shot" role="img" aria-label="Gelb-grüner Trekkingrucksack" style="background:radial-gradient(#c8d630,#7c7a5a 55%,#fff 70%)"></div><a class="more">weiter ...</a></div>
</section>

<section class="abs panel info">
  <h2 style="left:22px;top:29px">Über uns</h2>
  <p class="copy" style="left:22px;top:53px">to omniendia plandempe ped eumet esci optatquae dolestia sunt. Rionsequo et, nimintio te culpa dolenditat aute repudant hit rehent lam, aut etum excero ipis enihilibus, cus maxim renditate odit qui quo quas eat eicieni hitatur modiam re dipieni hilloria si occaborias sitatiur</p>
  <h2 style="left:22px;top:158px">Newsletter</h2>
  <p class="copy" style="left:22px;top:182px">to omniendia plandempe ped eumet esci optatquae dolestia sunt. Rionsequo et, nimintio te culpa dolenditat aute repudant hit rehent lam, aut etum excero ipis enihilibus, cus maxim renditate odit qui quo quas eat eicieni hitatur modiam re dipieni hilloria si occaborias sitatiur</p>
  <div class="newsletter-form"><div class="field">E-Mail Adresse</div><div class="send">senden</div></div>
  <div class="divider" style="left:344px;top:22px;height:278px"></div>
  <h2 style="left:355px;top:29px">Neuigkeiten</h2>
  <article class="news" style="top:49px">
    <div class="date">14<br>JUN</div>
    <h4>Im ratur sim re voluptam adi conserr uptatet reictis litasincia quatur modiam erum cone consecus</h4>
    <p>to omniendia plandempe ped eumet esci optatquae dolestia sunt. Rionsequo et, nimintio te culpa dolenditat aute repudant hit rehent lam, aut etum excero ipis enihilibus, cus maxim renditate odit qui quo quas eat eicieni hitatur modiam re dipieni hilloria si occaborias sitatiur</p>
    <a class="more">weiter ...</a>
  </article>
  <article class="news" style="top:183px">
    <div class="date">10<br>JUN</div>
    <h4>Im ratur sim re voluptam adi conserr uptatet reictis litasincia quatur modiam erum cone consecus</h4>
    <p>to omniendia plandempe ped eumet esci optatquae dolestia sunt. Rionsequo et, nimintio te culpa dolenditat aute repudant hit rehent lam, aut etum excero ipis enihilibus, cus maxim renditate odit qui quo quas eat eicieni hitatur modiam re dipieni hilloria si occaborias sitatiur</p>
    <a class="more">weiter ...</a>
  </article>
</section>

<footer class="abs footer">
  <h5 style="left:160px">Service</h5>
  <div class="col" style="left:160px;top:44px">Straße, Hausnummer<br>PLZ, Ort<br><br>Telefon (12) - 345 678 99<br>Fax (12) - 345 678 99<br>Emailemail@email.com</div>
  <div class="social" style="left:160px"></div>
  <div class="social" style="left:183px"></div>
  <div class="social" style="left:206px"></div>
  <div class="fdiv" style="left:315px"></div>
  <h5 style="left:327px">Zahlungsarten</h5>
  <div class="pay" style="left:328px;top:39px">Konto</div>
  <div class="pay" style="left:367px;top:39px">Karte</div>
  <div class="pay" style="left:328px;top:63px">Bank</div>
  <div class="pay" style="left:367px;top:63px">Debit</div>
  <div class="pay" style="left:328px;top:87px">Kasse</div>
  <div class="fdiv" style="left:483px"></div>
  <h5 style="left:495px">Kategorien</h5>
  <ul class="col cats" style="left:495px;top:44px"><li>Kategorie</li><li>Kategorie</li><li>Kategorie</li><li>Kategorie</li><li>Kategorie</li><li>Kategorie</li><li>Kategorie</li></ul>
  <div class="fdiv" style="left:650px"></div>
  <h5 style="left:660px">Tweets</h5>
  <div class="col" style="left:660px;top:45px"><span class="tweet-date">7 March 2013</span><br>to omniendia plandempe ped<br>eumet esci optatquae dolestia<br><br><span class="tweet-date">7 March 2013</span><br>to omniendia plandempe ped<br>eumet esci optatquae dolestia</div>
</footer>

<div class="abs bottom">
  <div class="legal">© Copyright 2013 VORMA</div>
  <div class="links">Home<span>|</span>Kontakt<span>|</span>Impressum</div>
</div>

</body>
</html>
```